Copperfield Ridge Dental business card

Business card would have following info:

Harold T. Quenneville, DMD, FAGD
General Dentist
email: office@copperfieldridgedental.com
phone: 413-867-3094
fax: 413-867-3094
website: copperfieldridgedental.com

second side would have lines for:

appointment date
appointment time

```html
<!DOCTYPE html>
<html lang="en">
<head>
<meta charset="utf-8">
<title>Copperfield Ridge Dental – Business Card</title>
<link href="https://fonts.googleapis.com/css2?family=Arimo:wght@400;700&display=swap" rel="stylesheet">
<style>
  :root {
    --backdrop: #989898;
    --card: #ffffff;
    --ink: #2b2b2b;
    --ink-soft: #3a3a3a;
    --accent-bar: #333333;
    --rule: #333333;
  }
  html, body {
    margin: 0;
    padding: 0;
    width: 1200px;
    height: 1059px;
    overflow: hidden;
    background: var(--backdrop);
    font-family: "Arimo", Arial, sans-serif;
  }
  .card {
    position: absolute;
    width: 690px;
    height: 392px;
    background: var(--card);
    border-radius: 22px;
    overflow: hidden;
  }
  .card--front { left: 255px; top: 89px; }
  .card--back  { left: 255px; top: 569px; }

  .identity {
    position: absolute;
    right: 42px;
    top: 56px;
    text-align: right;
    color: var(--ink);
  }
  .identity__name {
    margin: 0;
    font-weight: 700;
    font-size: 25px;
    line-height: 31px;
    letter-spacing: 0.2px;
    text-transform: uppercase;
  }
  .identity__role {
    margin: 0;
    font-size: 20px;
    line-height: 24px;
    color: var(--ink-soft);
  }
  .accent-bar {
    position: absolute;
    right: 0;
    top: 63px;
    width: 25px;
    height: 72px;
    background: var(--accent-bar);
  }

  .contact-list {
    position: absolute;
    left: 43px;
    top: 250px;
    margin: 0;
    padding: 0;
    list-style: none;
    color: var(--ink);
    font-size: 17.5px;
  }
  .contact-list li {
    display: flex;
    align-items: center;
    height: 26.5px;
  }
  .contact-list svg {
    width: 13px;
    height: 13px;
    margin-right: 8px;
    fill: var(--ink);
    flex: none;
  }

  .appointment {
    position: absolute;
    left: 45px;
    width: 605px;
    color: var(--ink-soft);
    font-size: 18px;
  }
  .appointment__label { display: block; }
  .appointment__line {
    display: block;
    margin-top: 14px;
    border-top: 1.2px solid var(--rule);
  }
  .appointment--date { top: 126px; }
  .appointment--time { top: 222px; }
</style>
</head>
<body>

<section class="card card--front" aria-label="Card front">
  <div class="identity">
    <p class="identity__name">Harold T. Quenneville<br>DMD, FAGD</p>
    <p class="identity__role">General Dentist</p>
  </div>
  <div class="accent-bar"></div>

  <ul class="contact-list">
    <li>
      <svg viewBox="0 0 16 16" aria-hidden="true"><path d="M1 6c0-2 3-3.5 7-3.5S15 4 15 6v1.3h-3.5V5.6c-1-.5-6-.5-7 0v1.7H1z"/><path d="M4 8l1.5-2h5L12 8v5.5H4z"/></svg>
      413-867-3094
    </li>
    <li>
      <svg viewBox="0 0 16 16" aria-hidden="true"><rect x="4" y="1" width="8" height="4"/><rect x="1" y="5.5" width="14" height="6" rx="1"/><rect x="4" y="10" width="8" height="5" fill="#fff" stroke="#2b2b2b" stroke-width="1.4"/></svg>
      413-867-3094
    </li>
    <li>
      <svg viewBox="0 0 16 16" aria-hidden="true"><path d="M1 7l7-5 7 5v8H1z"/><path d="M3 7.5h10L8 11z" fill="#fff"/></svg>
      office@copperfieldridgedental.com
    </li>
    <li>
      <svg viewBox="0 0 16 16" aria-hidden="true"><circle cx="8" cy="8" r="7"/><path d="M4 4.5c2 .5 2 2 3.5 2.5s.5 2-1 2.5-.5 3 .5 4c-2 0-4-2-4.5-4S3 5 4 4.5zM10 3c1 1 2.5 1 3 3-1 .5-2 0-2.5 1.5S9 9 9 7.5 9 4 10 3z" fill="#fff"/></svg>
      www.copperfieldridgedental.com
    </li>
  </ul>
</section>

<section class="card card--back" aria-label="Card back">
  <div class="appointment appointment--date">
    <span class="appointment__label">Appointment Date :</span>
    <span class="appointment__line"></span>
  </div>
  <div class="appointment appointment--time">
    <span class="appointment__label">Appointment Time :</span>
    <span class="appointment__line"></span>
  </div>
</section>

</body>
</html>
```